HR consultancy website - Wordpress Design Project

We need a wordpress design for a new company based in Belgium called Brivoltex. We propose HR consultancy services focused on employees' engagement (motivation). We target corporations from 100 to 1000+ employees mainly in Europe.
We need a new design for our existing website (www.brivoltex.eu).
We find the current design too static and outdated and we are looking for a more appealing look & feel.
Nevertheless, it has also to be sober.
The colours of the logo (dark blue, purple and light grey) should be preferrably used.
The content structure and the texts remain the same.

Target Market(s)

HR managers, general managers of SME's, higher education

Industry/Entity Type

It Company

Requirements
Must have
• No specific functionalities, except a contact form.

```html
<!DOCTYPE html>
<html lang="en">
<head>
<meta charset="utf-8">
<title>Brivoltex – HR Consultancy</title>
<link rel="stylesheet" href="https://fonts.googleapis.com/css2?family=Oswald:wght@400&family=Signika:wght@300;400&family=PT+Sans:wght@400;700&display=swap">
<style>
:root{
  --page:#f0f0f0;
  --white:#ffffff;
  --navy:#0e3f7e;
  --navy-dark:#0a2f63;
  --circle:#12386c;
  --pink:#d42e76;
  --pink-light:#e24888;
  --text-blue:#123b72;
  --grey-text:#333333;
  --logo-grey:#bcb4ab;
  --reset:#5e5e5e;
}
*{box-sizing:border-box;margin:0;padding:0}
html,body{width:1158px;height:1200px;overflow:hidden}
body{background:var(--page);font-family:"PT Sans",sans-serif;position:relative;color:var(--grey-text)}
.abs{position:absolute}
.header{left:0;top:0;width:1158px;height:165px;background:linear-gradient(#fafafa,#ebebeb);border-top:4px solid #d8d8d8}
.brand{left:120px;top:44px;font-family:"PT Sans",sans-serif;font-size:42px;color:var(--logo-grey);letter-spacing:1px}
.search{left:802px;top:72px;width:226px;height:28px;border:1px solid #d5d5d5;border-radius:14px;background:#fff;font-size:11px;color:#234;display:flex;align-items:center;padding-left:10px;gap:8px}
.nav{left:119px;top:111px;width:921px;height:54px;background:linear-gradient(#154c91,var(--navy-dark));display:flex}
.nav a{font-family:"Oswald",sans-serif;font-size:15px;color:#fff;text-decoration:none;height:54px;display:flex;align-items:center;padding:0 22px 0 35px;border-right:1px solid #2a5a98}
.nav a + a{padding-left:23px}
.main{left:119px;top:165px;width:921px;height:973px;background:var(--white)}
.hero-frame{left:119px;top:165px;width:921px;height:313px;border:1px solid #e2e2e2;background:#fff}
.hero-photo{left:130px;top:173px;width:620px;height:300px;background:linear-gradient(160deg,#5f94d0 0%,#b9d4ef 55%,#7fa6c9 80%,#e6eef4 100%)}
.hero-panel{left:753px;top:173px;width:280px;height:300px;background:linear-gradient(#dc3f80,var(--pink));color:#fff;padding:35px 14px 0 31px}
.hero-panel h1{font-family:"Signika",sans-serif;font-weight:300;font-size:21px;line-height:29px;white-space:nowrap}
.hero-panel .lead{font-weight:700;font-size:12.5px;line-height:18px;margin-top:5px}
.hero-panel p{font-size:10px;line-height:18px;margin-top:1px}
.pill{display:inline-block;margin-top:11px;background:var(--pink-light);border-radius:13px;font-size:10.5px;font-weight:700;padding:6px 17px;color:#fff}
.steps{left:131px;top:492px;width:898px;height:157px;background:linear-gradient(#f3f3f3,#fbfbfb 40%,#f1f1f1);display:flex}
.step{position:relative;border-right:1px solid #e3e3e3;padding:37px 0 0 64px}
.step:last-child{border-right:none}
.step .num{position:absolute;left:24px;top:37px;width:34px;height:34px;border-radius:50%;background:var(--circle);color:#fff;font-family:"Signika",sans-serif;font-size:19px;display:flex;align-items:center;justify-content:center}
.step h2{font-family:"Signika",sans-serif;font-weight:300;font-size:18px;color:var(--text-blue);margin-top:-6px}
.step p{font-size:11px;line-height:18px;color:var(--text-blue);margin-top:2px}
.card-img{width:266px;height:113px;border:3px solid #fff;box-shadow:0 0 0 1px #e4e4e4}
.card h3{font-family:"Signika",sans-serif;font-weight:300;font-size:15.5px;color:#333;margin:14px 0 0 5px}
.card p{font-size:11px;line-height:16px;margin:6px 0 0 5px;color:#333}
.form{left:725px;top:678px;width:298px;height:413px;border:1px solid #e6e6e6;background:linear-gradient(#f6f6f6,#fff 40%,#f7f7f7);padding:16px 0 0 21px}
.form h2{font-family:"Signika",sans-serif;font-weight:400;font-size:19px;color:var(--pink)}
.form label{display:block;font-size:10.5px;line-height:13px;color:#333;margin-top:8px}
.form h2 + label{margin-top:14px}
.form .field{width:255px;height:27px;border:1px solid #cfcfcf;background:#fff;margin-top:6px}
.form .area{height:120px}
.btns{display:flex;gap:6px;margin-top:12px;margin-left:6px}
.btn{width:83px;height:29px;border-radius:15px;color:#fff;font-family:"Signika",sans-serif;font-size:15px;display:flex;align-items:center;justify-content:center}
.btn.submit{background:var(--pink)}
.btn.reset{background:var(--reset)}
.footer{top:1153px;font-size:10.5px;color:#333}
.footer span{margin:0 4px;color:#777}
</style>
</head>
<body>
<div class="abs header"></div>
<div class="abs brand">BRIVOLTEX</div>
<div class="abs search">
  <svg width="14" height="14" viewBox="0 0 14 14"><circle cx="5.5" cy="5.5" r="4.2" fill="none" stroke="#0e3f7e" stroke-width="2"/><line x1="8.6" y1="8.6" x2="12.5" y2="12.5" stroke="#0e3f7e" stroke-width="2.4"/></svg>
  <span>Enter keyword..</span>
</div>
<nav class="abs nav">
  <a href="#">HOME</a><a href="#">OUR MISSION</a><a href="#">ABOUT US</a><a href="#">CONTACT US</a>
</nav>

<div class="abs main"></div>
<div class="abs hero-frame"></div>
<div class="abs hero-photo" role="img" aria-label="Smiling businessman walking on a beach under a blue sky"></div>
<div class="abs hero-panel">
  <h1>Brivoltex Boosts<br>Company Performances</h1>
  <div class="lead">Lorem ipsum dolor sit amet, consec tetuer adipiscing elit.</div>
  <p>Nullam enim leo, egestas id, condimentum at, laoreet mattis, massa. Sed eleifend nonummy diam. Praesent mauris ante, elementum et, bibendum at, posuere sit amet, nibh. Fusce id felis. Vivamus sollicitudin metus eget eros.</p>
  <span class="pill">Our Mission</span>
</div>

<section class="abs steps">
  <div class="step" style="width:227px"><span class="num">1</span><h2>EVALUATION</h2><p>Only between 13 and 21% of<br>employees are actively<br>engaged in their job.</p></div>
  <div class="step" style="width:221px;padding-left:61px"><span class="num">2</span><h2>STRATEGY</h2><p>Brivoltex helps corporate<br>leaders get the best<br>contribution from employees.</p></div>
  <div class="step" style="width:216px;padding-left:60px"><span class="num" style="left:16px">3</span><h2>PROCESS</h2><p>Our ERM tool creates an HR<br>engagement cycle to<br>encourage line managers to<br>take initiatives</p></div>
  <div class="step" style="width:234px;padding-left:59px"><span class="num" style="left:19px">4</span><h2>IMPACT</h2><p>Our ERM tool measures impact<br>by creating an index which can<br>then be used for comparison<br>over time.</p></div>
</section>

<div class="abs card" style="left:144px;top:681px">
  <div class="card-img" role="img" aria-label="Business people shaking hands" style="background:linear-gradient(135deg,#1b2c52,#8fa4c4 50%,#23395f)"></div>
  <h3>Consulting Services</h3><p>Ut ante enim, dapibus malesuada, fringilla eu,<br>condimentum quis, tellus vel dolor.</p>
</div>
<div class="abs card" style="left:433px;top:681px">
  <div class="card-img" role="img" aria-label="Smiling man and woman portrait" style="background:linear-gradient(90deg,#9aa4ae,#e9ecef 55%,#c9d2dc)"></div>
  <h3>Employee Support</h3><p>Ut ante enim, dapibus malesuada, fringilla eu,<br>condimentum quis, tellus vel dolor.</p>
</div>
<div class="abs card" style="left:144px;top:885px">
  <div class="card-img" role="img" aria-label="Blue telephone on a newspaper" style="background:linear-gradient(#2f6fc1,#86b3e6 50%,#d7e6f5)"></div>
  <h3>Recent Blog</h3><p>Ut ante enim, dapibus malesuada, fringilla eu,<br>condimentum quis, tellus vel dolor.</p>
</div>
<div class="abs card" style="left:433px;top:885px">
  <div class="card-img" role="img" aria-label="Hand sketching a process flow chart" style="background:linear-gradient(135deg,#f4f4f4,#e2e2e2 60%,#f7f7f7)"></div>
  <h3>Term and Process</h3><p>Ut ante enim, dapibus malesuada, fringilla eu,<br>condimentum quis, tellus vel dolor.</p>
</div>

<form class="abs form">
  <h2>Fill Our Contact Form</h2>
  <label>Full Name:</label><div class="field"></div>
  <label>Email address:</label><div class="field"></div>
  <label>Phone no:</label><div class="field"></div>
  <label>Message/query:</label><div class="field area"></div>
  <div class="btns"><span class="btn submit">Submit</span><span class="btn reset">Reset</span></div>
</form>

<div class="abs footer" style="left:125px">Copyright © 2012 Company Name <span>|</span> Term of Use</div>
<div class="abs footer" style="right:128px">Home <span>|</span> Mission <span>|</span> About Us <span>|</span> Contact</div>
</body>
</html>
```